3 out of 100 people will get deadly skin cancer - we need a great illustration that shows this!

We put together a prototype image that communicates lifetime skin cancer risk. (see attached). We are looking for illustrators who can take make a new/better/cooler graphic that communicates this idea. It could be as simple as a superior illustration of the graphic we have or illustrators can propose a completely different idea.What should the illustration communicate?U.S. adults have a lifetime risk of developing skin cancer of 1 in 5. But we don't want to show 1 in 5; we want to show that number in a larger group. For example, in the attached illustration we show 20 in 100 people get skin cancer (i.e., 100 beach towels/umbrellas and 20 of them are red). Research has shown that people are more likely to accurately understand numbers like this when you convey them for larger groups (i.e., 20 out of 100 rather than 1 out of 5). U.S. adults also have a lifetime risk of 2.3% of developing the deadliest form of skin cancer (melanoma). In other words, approximately 3 in 100 people will develop melanoma in their lifetime. Ideally, a single image will convey both lifetime skin cancer risk (20 in 100) and melanoma risk (3 in 100). We will award a top three as follows: 1st place = $300, 2nd place = $250, third place = $200. We will also buy any design beyond 3rd place that we like for $100. For example, we purchased 24 designs in our last contest on Artmarketly.This research is supported by funding from the Corvane Institute of Science.

Target Market(s)

The U.S. public; individuals at high risk of developing skin cancer

Industry/Entity Type

Medicine

Colors

Designer to choose colors to be used in the design.

Requirements
Must have
• an original illustration that conveys both lifetime risk of developing skin cancer (20 in 100) and melanoma (3 in 100).
Nice to have
• It can be beach towels and umbrellas, just like our prototype, or the designers can pitch an original idea. Imagery can be realistic or cartoonish (or something in between). It should be illustrations, though. Not edited photos. The image should be in color (no black and white illustrations).
Should not have
• Photos. Clip art. Free vector images.
• We are looking for original illustrations created by the designer.

```html
<!DOCTYPE html>
<html lang="en">
<head>
<meta charset="utf-8">
<title>How Likely Are You to Get Skin Cancer?</title>
<link rel="stylesheet" href="https://fonts.googleapis.com/css2?family=Fjalla+One&display=swap">
<style>
  :root {
    --rose: #d95b67;
    --navy: #22345a;
    --cream: #f8ecd9;
    --sand: #e5c18a;
    --sea: #7fb3b8;
    --skin: #f0cf98;
  }
  * { margin: 0; padding: 0; box-sizing: border-box; }
  html, body { width: 849px; height: 1200px; overflow: hidden; background: var(--cream); }
  .poster {
    position: relative; width: 849px; height: 1200px; overflow: hidden;
    background: var(--cream);
    font-family: "Fjalla One", "Arial Narrow", sans-serif;
  }
  .header {
    position: absolute; left: 0; top: 0; width: 849px; height: 222px;
    background: var(--rose);
    display: flex; align-items: center; justify-content: center;
  }
  .header h1 {
    color: var(--cream); font-weight: 400; font-size: 56px; line-height: 1.22;
    text-align: center; letter-spacing: 1.5px; margin-top: 4px;
  }
  .sand-stripe { position: absolute; left: 0; top: 222px; width: 849px; height: 23px; background: var(--sand); }
  .sea-band {
    position: absolute; left: 0; top: 562px; width: 849px; height: 200px;
    background: var(--sea);
  }
  .beach-illustration {
    position: absolute; left: 243px; top: 290px; width: 360px; height: 398px;
    border-radius: 4px;
    background: linear-gradient(to bottom, #e99aa0 0%, var(--skin) 45%, #c99a80 100%);
  }
  .banner { position: absolute; left: 45px; top: 688px; width: 760px; height: 74px; }
  .banner svg { display: block; }
  .banner p {
    position: absolute; inset: 0; display: flex; align-items: center; justify-content: center;
    color: var(--cream); font-size: 43px; letter-spacing: 0.6px; padding-bottom: 2px;
  }
  .dash-line {
    position: absolute; top: 762px; height: 181px; width: 0;
    border-left: 4px dashed var(--rose);
  }
  .dash-line.left { left: 106px; }
  .dash-line.right { left: 739px; }
  .question {
    position: absolute; left: 188px; top: 797px;
    color: var(--rose); font-size: 23px; line-height: 1.5; white-space: nowrap;
  }
  .stat {
    position: absolute; top: 943px; height: 257px;
    display: flex; align-items: center;
  }
  .stat.melanoma { left: 0; width: 425px; background: var(--navy); }
  .stat.skin-cancer { left: 425px; width: 424px; background: var(--rose); }
  .stat-number { color: var(--cream); font-size: 118px; line-height: 1; }
  .melanoma .stat-number { margin-left: 66px; width: 81px; }
  .skin-cancer .stat-number { margin-left: 40px; width: 134px; }
  .stat-text { color: var(--cream); font-size: 27px; line-height: 1.38; letter-spacing: 0.4px; }
  .melanoma .highlight { color: var(--rose); }
  .skin-cancer .highlight { color: var(--navy); }
</style>
</head>
<body>
<main class="poster">
  <header class="header">
    <h1>HOW LIKELY ARE YOU TO<br>GET SKIN CANCER?</h1>
  </header>
  <div class="sand-stripe"></div>
  <div class="sea-band" role="img" aria-label="Sea with a gentle wave pattern"></div>
  <div class="beach-illustration" role="img" aria-label="Illustration of a woman in a striped sun hat and polka-dot swimsuit sitting on a wooden dock by the sea, seen from behind"></div>

  <div class="banner">
    <svg width="760" height="74" viewBox="0 0 760 74" aria-hidden="true">
      <polygon points="0,0 760,0 730,37 760,74 0,74 30,37" fill="#d95b67"/>
    </svg>
    <p>Let’s say 100 people go to the beach</p>
  </div>

  <div class="dash-line left"></div>
  <div class="dash-line right"></div>
  <p class="question">How many will develop skin cancer in their<br>lifetime? How many will develop melanoma,<br>the deadliest form of skin cancer?</p>

  <section class="stat melanoma">
    <span class="stat-number">3</span>
    <p class="stat-text">OUT OF 100<br>US ADULTS HAVE A<br>RISK OF DEVELOPING<br><span class="highlight">MELANOMA</span></p>
  </section>
  <section class="stat skin-cancer">
    <span class="stat-number">20</span>
    <p class="stat-text">OUT OF 100<br>US ADULTS HAVE A<br>RISK OF DEVELOPING<br><span class="highlight">SKIN CANCER</span></p>
  </section>
</main>
</body>
</html>
```